New bussiness card, using company logo.
Lachlan Voss
Manager/Director
Birch Property Developments
Po Box 4657
Marrowby Central
Wyn
0455 386 218
lachlan@birchpropertydevelopments
eye catching, vibrant colours, professional

```html
<!DOCTYPE html>
<html lang="en">
<head>
<meta charset="utf-8">
<title>Birch Property Developments – Business Card</title>
<link href="https://fonts.googleapis.com/css2?family=Open+Sans:wght@400;600;700&display=swap" rel="stylesheet">
<style>
  :root {
    --backdrop: #3a3f3d;
    --card-white: #f4f4f2;
    --brand-red: #d01f28;
    --deep-red: #a3141c;
    --glow: #f07a5c;
    --stripe-grey: #6b6b6b;
    --text-light: #ffffff;
  }
  * { box-sizing: border-box; margin: 0; padding: 0; }
  html, body {
    width: 1200px; height: 900px; overflow: hidden;
    background: var(--backdrop);
    font-family: "Open Sans", Arial, sans-serif;
  }
  .sheet {
    width: 1200px; height: 900px;
    display: flex; flex-direction: column;
    align-items: center; justify-content: center; gap: 56px;
  }
  .card {
    position: relative;
    width: 640px; height: 356px;
    background: var(--card-white);
    overflow: hidden;
    box-shadow: 0 10px 26px rgba(0,0,0,.35);
  }
  .card__band {
    position: absolute; left: 0; right: 0; bottom: 0;
    border-top: 6px solid var(--stripe-grey);
    background: radial-gradient(ellipse 260px 150px at 50% 10%, var(--glow) 0%, var(--brand-red) 55%, var(--deep-red) 100%);
  }
  .card--front .card__band { top: 186px; }
  .card--back .card__band { top: 200px; }

  .brand-name {
    position: absolute; top: 62px; left: 0; right: 0;
    display: flex; align-items: center; justify-content: center; gap: 12px;
    color: var(--brand-red);
    font-weight: 700; font-size: 30px; letter-spacing: .5px;
  }
  .brand-name__mark {
    width: 22px; height: 22px; background: var(--brand-red);
  }

  .holder {
    position: absolute; top: 18px; right: 26px; text-align: right;
    color: var(--text-light);
  }
  .holder__name { font-weight: 700; font-size: 17px; text-transform: uppercase; }
  .holder__role { font-size: 14px; }

  .contact {
    position: absolute; top: 14px; left: 26px;
    color: var(--text-light); font-size: 13.5px; line-height: 1.15;
  }
  .contact__company { margin-left: 20px; margin-bottom: 12px; text-transform: uppercase; font-size: 13.5px; }
  .contact__row { display: flex; align-items: flex-start; gap: 10px; margin-bottom: 6px; }
  .contact__row--tight { margin-bottom: 1px; align-items: center; }
  .contact__icon { width: 12px; height: 12px; flex: none; margin-top: 2px; fill: #f3d7d7; }

  .web-address {
    position: absolute; top: 62px; left: 0; right: 0; text-align: center;
    color: var(--text-light); font-size: 19px;
  }
  .web-address strong { font-weight: 700; }
</style>
</head>
<body>
<main class="sheet">

  <section class="card card--front" aria-label="Business card front">
    <div class="brand-name"><span class="brand-name__mark"></span>Birch Property Developments</div>
    <div class="card__band">
      <div class="holder">
        <p class="holder__name">Lachlan Voss</p>
        <p class="holder__role">Manager/Director</p>
      </div>
      <div class="contact">
        <p class="contact__company">Birch Property Developments</p>
        <div class="contact__row">
          <svg class="contact__icon" viewBox="0 0 12 12" aria-hidden="true"><path d="M6 0a4 4 0 0 0-4 4c0 3 4 8 4 8s4-5 4-8a4 4 0 0 0-4-4zm0 5.6A1.6 1.6 0 1 1 6 2.4a1.6 1.6 0 0 1 0 3.2z"/></svg>
          <p>P.O. Box 4657<br>Marrowby Central<br>Wyn</p>
        </div>
        <div class="contact__row">
          <svg class="contact__icon" viewBox="0 0 12 12" aria-hidden="true"><path d="M2.5 0.5 4.5 3 3.4 4.3c.8 1.8 2.4 3.4 4.3 4.3L9 7.5l2.5 2-1 1.8C5.5 11.5.5 6.5.7 1.5z"/></svg>
          <p>0455 386 218</p>
        </div>
        <div class="contact__row contact__row--tight">
          <svg class="contact__icon" viewBox="0 0 12 12" aria-hidden="true"><path d="M0 2h12v8H0zm1 1v.4l5 3.2 5-3.2V3zm0 1.6V9h10V4.6L6 7.8z"/></svg>
          <p>lachlan@birchpropertydevelopments.au</p>
        </div>
        <div class="contact__row contact__row--tight">
          <svg class="contact__icon" viewBox="0 0 12 12" aria-hidden="true"><circle cx="6" cy="6" r="5.5"/><path d="M.5 6h11M6 .5c-3 3-3 8 0 11M6 .5c3 3 3 8 0 11" stroke="#a3141c" stroke-width=".9" fill="none"/></svg>
          <p>www.birchpropertydevelopments.au</p>
        </div>
      </div>
    </div>
  </section>

  <section class="card card--back" aria-label="Business card back">
    <div class="card__band">
      <p class="web-address">www.<strong>BirchPropertyDevelopments</strong>.au</p>
    </div>
  </section>

</main>
</body>
</html>
```